Etiketten für Imkerei
Zielgruppe
Wir sind eine Imkerei in München. Die Zielgrppe sind Menschen, die lokale Produkte wertschätzen, beim Produzenten gern direkt und auf Märkten einkaufen.
Hallo,
wir benötigen ein universelles Design für Honiggläser-Etiketten, das für verschiedene Sorten verwendet werden kann. Das vorhanden Logo soll im Design aufgenommen werden. Im Logo reicht der Name: Imkerei-Brunntal.

```html
<!DOCTYPE html>
<html lang="de">
<head>
<meta charset="utf-8">
<title>Etikett Waldhonig – Imkerei Brunntal</title>
<link href="https://fonts.googleapis.com/css2?family=Great+Vibes&family=PT+Sans:wght@400;700&display=swap" rel="stylesheet">
<style>
  :root {
    --paper: #ffffff;
    --honey: #fecc02;
    --honey-band: #fdd95e;
    --comb-tone: rgba(255, 238, 150, 0.75);
    --comb-edge: rgba(255, 238, 150, 0);
    --cream: #fdf6e0;
    --ink: #1a1a1a;
    --white: #ffffff;
  }
  * { margin: 0; padding: 0; box-sizing: border-box; }
  html, body {
    width: 849px;
    height: 1200px;
    overflow: hidden;
    background: var(--paper);
  }
  .canvas {
    position: relative;
    width: 849px;
    height: 1200px;
  }
  .label {
    position: absolute;
    left: 122px;
    top: 120px;
    width: 611px;
    height: 283px;
    background: var(--honey);
    overflow: hidden;
    font-family: "PT Sans", sans-serif;
  }
  .comb-area {
    position: absolute;
    border-radius: 22px;
    background: radial-gradient(ellipse at center, var(--comb-tone) 0%, var(--comb-tone) 45%, var(--comb-edge) 100%);
  }
  .comb-area--left   { left: -10px; top: -10px; width: 150px; height: 185px; }
  .comb-area--right  { left: 325px; top: 20px;  width: 230px; height: 275px; }
  .comb-area--far    { left: 440px; top: 15px;  width: 100px; height: 80px; }
  .comb-area--edge   { left: 535px; top: 185px; width: 80px;  height: 100px; }
  .comb-area--bottom { left: 140px; top: 214px; width: 85px;  height: 75px; }
  .brand {
    position: absolute;
    left: 135px;
    top: 70px;
    display: flex;
    align-items: center;
    gap: 12px;
  }
  .brand__mark {
    width: 62px;
    height: 62px;
    background: var(--ink);
  }
  .brand__name {
    font-size: 28px;
    line-height: 30px;
    font-weight: 400;
    color: var(--ink);
    text-align: right;
  }
  .band {
    position: absolute;
    left: 0;
    top: 181px;
    width: 100%;
    height: 34px;
    background: var(--honey-band);
  }
  .variety-plate {
    position: absolute;
    left: 201px;
    top: 183px;
    width: 182px;
    height: 32px;
  }
  .variety-plate svg {
    position: absolute;
    inset: 0;
  }
  .variety-plate__name {
    position: relative;
    display: block;
    text-align: center;
    font-family: "Great Vibes", cursive;
    font-size: 27px;
    line-height: 32px;
    color: var(--ink);
  }
  .weight {
    position: absolute;
    left: 17px;
    top: 246px;
    font-size: 12.5px;
    color: var(--ink);
  }
  .description {
    position: absolute;
    right: 38px;
    top: 76px;
    width: 140px;
    text-align: right;
    color: var(--white);
  }
  .description__title {
    font-family: "Great Vibes", cursive;
    font-size: 17px;
    line-height: 18px;
  }
  .description__text {
    font-size: 8.8px;
    line-height: 11.4px;
  }
</style>
</head>
<body>
<div class="canvas">
  <section class="label">
    <div class="comb-area comb-area--left" role="img" aria-label="Wabenmuster aus weißen Sechseck-Umrissen"></div>
    <div class="comb-area comb-area--right" role="img" aria-label="Wabenmuster aus weißen Sechseck-Umrissen"></div>
    <div class="comb-area comb-area--far" role="img" aria-label="Wabenmuster aus weißen Sechseck-Umrissen"></div>

    <div class="band"></div>

    <div class="comb-area comb-area--edge" role="img" aria-label="Wabenmuster aus weißen Sechseck-Umrissen"></div>
    <div class="comb-area comb-area--bottom" role="img" aria-label="Wabenmuster aus weißen Sechseck-Umrissen"></div>

    <div class="brand">
      <span class="brand__mark"></span>
      <span class="brand__name">Imkerei<br>Brunntal</span>
    </div>

    <div class="variety-plate">
      <svg width="182" height="32" viewBox="0 0 182 32" aria-hidden="true">
        <polygon points="12,0 170,0 182,16 170,32 12,32 0,16" fill="var(--cream)"/>
      </svg>
      <span class="variety-plate__name">Waldhonig</span>
    </div>

    <p class="weight">500 gr</p>

    <div class="description">
      <p class="description__title">Waldhonig,</p>
      <p class="description__text">
        flüssig, 500 gr:<br>
        Mit Beginn der Holunder-<br>
        blüte ziehen die Völker in<br>
        Waldgebiete um,<br>
        um dort auf die Suche<br>
        nach dem besonderen<br>
        Waldhonig zu gehen.
      </p>
    </div>
  </section>
</div>
</body>
</html>
```